VENTURE CAPITAL GROUP BUSINESS CARD DESIGN

Venture Capital Group based in SF looking for a bold business card design. No trendy colour explosion, 3D effects etc. Just "simple" optical effects. Works on your brain, keeps your eye focused and sticks to your mind.
Target Market(s)
Technology startups
Industry/Entity Type
Venture Capital
Contact Information for Business Card
BARTHOLOMEW ELLING
MANAGING PARTNER
817 FERN ST SAN FRANCISCO, CA 94111
415.555.0142 O
415.555.0187 F
415.555.0236 C
bart@quillbrookfunds.example

```html
<!DOCTYPE html>
<html lang="en">
<head>
<meta charset="utf-8">
<title>Quillbrook Capital Group – Business Card</title>
<link href="https://fonts.googleapis.com/css2?family=Open+Sans:wght@400;600;700;800&display=swap" rel="stylesheet">
<style>
  :root {
    --forest: #0f5229;
    --forest-deep: #0b4420;
    --leaf: #2fae4a;
    --white: #ffffff;
    --silver: #c9c9c9;
    --backdrop: #e9ebe8;
  }
  * { box-sizing: border-box; margin: 0; padding: 0; }
  html, body { width: 1200px; height: 900px; overflow: hidden; }
  body {
    background: var(--backdrop);
    font-family: "Open Sans", Arial, sans-serif;
    display: flex;
    flex-direction: column;
    align-items: center;
    justify-content: center;
    gap: 56px;
  }
  .card {
    position: relative;
    width: 620px;
    height: 354px;
    border-radius: 22px;
    overflow: hidden;
    box-shadow: 0 10px 30px rgba(0,0,0,0.18);
  }

  /* Back side */
  .card-back {
    background: var(--forest);
    display: flex;
    flex-direction: column;
    align-items: center;
    justify-content: center;
    gap: 22px;
  }
  .brand-dot {
    width: 112px; height: 112px; border-radius: 50%;
    background: radial-gradient(circle at 40% 35%, #ffffff 0%, #e6e6e6 60%, var(--silver) 100%);
  }
  .card-back .brand-name {
    color: var(--white);
    font-weight: 600;
    font-size: 30px;
    letter-spacing: 2px;
  }

  /* Front side */
  .card-front { background: var(--white); }
  .card-front .wave { position: absolute; inset: 0; width: 100%; height: 100%; }
  .card-front .brand-dot {
    position: absolute; left: 440px; top: 22px;
    width: 128px; height: 128px;
  }
  .identity {
    position: absolute; left: 40px; top: 118px;
  }
  .card-front .brand-name {
    color: var(--forest);
    font-weight: 600;
    font-size: 25px;
    letter-spacing: 1px;
    margin-bottom: 26px;
  }
  .person-name {
    color: var(--forest);
    font-weight: 800;
    font-size: 22px;
    letter-spacing: 0.5px;
  }
  .person-role {
    color: var(--leaf);
    font-weight: 700;
    font-size: 13px;
    letter-spacing: 0.5px;
    margin-bottom: 12px;
  }
  .address {
    color: var(--forest);
    font-weight: 600;
    font-size: 13px;
    line-height: 1.35;
    width: 170px;
  }
  .contacts {
    position: absolute; right: 26px; top: 168px;
    list-style: none;
    color: var(--white);
    font-size: 13px;
    font-weight: 600;
    text-align: right;
  }
  .contacts li {
    display: flex; justify-content: flex-end; align-items: center;
    gap: 8px; line-height: 20px;
  }
  .contacts svg { width: 11px; height: 11px; fill: none; stroke: var(--leaf); stroke-width: 1.6; }
  .email {
    position: absolute; right: 26px; bottom: 48px;
    color: var(--white);
    font-size: 14px;
    font-weight: 600;
  }
</style>
</head>
<body>

  <section class="card card-back">
    <div class="brand-dot"></div>
    <div class="brand-name">QUILLBROOK CAPITAL GROUP</div>
  </section>

  <section class="card card-front">
    <svg class="wave" viewBox="0 0 620 354" preserveAspectRatio="none" aria-hidden="true">
      <path d="M620 70 L505 70 C455 70 470 190 420 250 C370 315 190 300 0 312 L0 354 L620 354 Z" fill="var(--forest)"/>
      <path d="M505 62 C445 62 462 185 410 246 C362 302 190 292 0 300 L0 310 C190 300 368 312 416 250 C466 190 452 72 505 72 L620 72 L620 62 Z" fill="var(--leaf)"/>
      <path d="M470 66 C430 100 440 200 395 250 C350 296 190 286 0 290 L0 295 C190 292 356 300 400 252 C446 202 436 104 474 68 Z" fill="var(--forest)"/>
      <path d="M0 325 C150 320 300 322 380 300 L380 306 C300 328 150 328 0 332 Z" fill="var(--leaf)"/>
    </svg>
    <div class="brand-dot"></div>

    <div class="identity">
      <div class="brand-name">QUILLBROOK CAPITAL GROUP</div>
      <div class="person-name">BARTHOLOMEW ELLING</div>
      <div class="person-role">MANAGING PARTNER</div>
      <div class="address">817 FERN ST SAN FRANCISCO, CA 94111</div>
    </div>

    <ul class="contacts">
      <li>415.555.0142
        <svg viewBox="0 0 12 12"><path d="M2 1 L4.5 1 L5.5 3.5 L4 4.5 C4.8 6.3 5.7 7.2 7.5 8 L8.5 6.5 L11 7.5 L11 10 C6 10.5 1.5 6 2 1 Z"/></svg>
      </li>
      <li>415.555.0187
        <svg viewBox="0 0 12 12"><rect x="2" y="4" width="8" height="5"/><path d="M3.5 4 V1.5 H8.5 V4 M3.5 9 V11 H8.5 V9"/></svg>
      </li>
      <li>415.555.0236
        <svg viewBox="0 0 12 12"><rect x="3" y="1" width="6" height="10" rx="1"/><path d="M5 9.2 H7"/></svg>
      </li>
    </ul>
    <div class="email">bart@quillbrookfunds.example
      <svg viewBox="0 0 12 12" style="width:11px;height:11px;fill:none;stroke:var(--leaf);stroke-width:1.6;margin-left:6px;vertical-align:middle"><rect x="1" y="2.5" width="10" height="7"/><path d="M1 2.5 L6 7 L11 2.5"/></svg>
    </div>
  </section>

</body>
</html>
```